Business card for STEADYWAVE

Please design professional business card for IT consulting firm STEADYWAVE INC.
Use logo attached.
Use information from sample qNode business card attached.
replace qnode inc with STEADYWAVE INC.
as well as qnodeinc.com with steadywave.example

```html
<!DOCTYPE html>
<html lang="en">
<head>
<meta charset="utf-8">
<title>STEADYWAVE business card</title>
<link href="https://fonts.googleapis.com/css2?family=Montserrat:wght@400;500;600;700&display=swap" rel="stylesheet">
<style>
  :root {
    --page-bg: #b9b9b9;
    --card-white: #ffffff;
    --ink: #1c1c1c;
    --ink-soft: #3a3a3a;
    --purple: #8a3f9c;
    --teal: #6fcbb5;
    --sky: #5ec3e6;
    --orange: #f0962e;
    --periwinkle: #7b8cc4;
  }
  * { margin: 0; padding: 0; box-sizing: border-box; }
  html, body {
    width: 1200px; height: 788px; overflow: hidden;
    background: var(--page-bg);
    font-family: "Montserrat", sans-serif;
  }
  .sheet {
    position: relative; width: 1200px; height: 788px;
    display: flex; align-items: center; justify-content: center; gap: 40px;
  }
  .card {
    position: relative; width: 540px; height: 309px;
    border-radius: 18px; overflow: hidden;
    box-shadow: 0 10px 28px rgba(0,0,0,0.25);
  }
  /* Front */
  .card-front { background: var(--card-white); }
  .wordmark {
    position: absolute; top: 38px; right: 38px;
    display: flex; align-items: center; gap: 10px;
    font-weight: 700; font-size: 31px; letter-spacing: 3px; color: var(--ink);
  }
  .wordmark-square { width: 14px; height: 14px; background: var(--teal); }
  .person {
    position: absolute; left: 0; top: 196px;
    padding-left: 26px;
  }
  .person-tab {
    position: absolute; left: 0; top: 2px; width: 9px; height: 44px;
    background: var(--purple);
  }
  .person-name {
    font-weight: 700; font-size: 15px; line-height: 1.2;
    letter-spacing: 0.6px; color: var(--purple); text-transform: uppercase;
  }
  .person-title {
    margin-top: 3px; font-weight: 500; font-size: 11.5px;
    letter-spacing: 0.8px; color: var(--ink-soft); text-transform: uppercase;
  }
  .contact {
    position: absolute; left: 282px; top: 104px;
    font-size: 11.2px; line-height: 1.5; color: var(--ink);
  }
  .contact-company {
    font-weight: 500; color: var(--teal); letter-spacing: 0.6px; text-transform: uppercase;
  }
  .contact-list { list-style: none; margin-top: 10px; }
  .contact-list li { display: flex; align-items: center; gap: 7px; }
  .contact-list svg { width: 11px; height: 11px; flex: none; }
  .edge-band {
    position: absolute; left: 0; right: 0; bottom: 0; height: 9px; display: flex;
  }
  .edge-band span { height: 100%; }
  .band-orange { width: 24%; background: var(--orange); }
  .band-sky { width: 26%; background: var(--sky); }
  .band-purple { width: 30%; background: var(--purple); }
  .band-teal { width: 20%; background: var(--teal); }
  /* Back */
  .card-back {
    background: linear-gradient(100deg,
      var(--orange) 0%, #c06e78 16%, var(--purple) 34%,
      var(--periwinkle) 55%, var(--sky) 74%, var(--teal) 100%);
  }
  .back-wordmark {
    position: absolute; inset: 0;
    display: flex; align-items: center; justify-content: center; gap: 14px;
    font-weight: 600; font-size: 44px; letter-spacing: 5px; color: var(--card-white);
  }
  .back-square { width: 20px; height: 20px; background: var(--card-white); }
</style>
</head>
<body>
<main class="sheet">
  <section class="card card-front" aria-label="Card front">
    <div class="wordmark">STEADYWAVE<span class="wordmark-square"></span></div>

    <div class="contact">
      <div class="contact-company">STEADYWAVE INC.</div>
      <div>1280 Harbourline Rd., Suite 204</div>
      <div>Brookvale, Ontario, A1B 2C3, Canada</div>
      <ul class="contact-list">
        <li>
          <svg viewBox="0 0 12 12" aria-hidden="true"><rect x="3" y="0.5" width="6" height="11" rx="1.2" fill="none" stroke="#f0962e" stroke-width="1.3"/><circle cx="6" cy="9.6" r="0.7" fill="#f0962e"/></svg>
          (555) 014-2290
        </li>
        <li>
          <svg viewBox="0 0 12 12" aria-hidden="true"><path d="M2.5 1.5 L4.5 1.5 L5.3 4 L4 5 C4.6 6.4 5.6 7.4 7 8 L8 6.7 L10.5 7.5 L10.5 9.5 C6 10 2 6 2.5 1.5 Z" fill="#f0962e"/></svg>
          (555) 018-3341 ext.201
        </li>
        <li>
          <svg viewBox="0 0 12 12" aria-hidden="true"><rect x="0.8" y="2.5" width="10.4" height="7" rx="1" fill="#f0962e"/><path d="M1.2 3 L6 6.6 L10.8 3" fill="none" stroke="#fff" stroke-width="1"/></svg>
          molenchuk@steadywave.example
        </li>
        <li>
          <svg viewBox="0 0 12 12" aria-hidden="true"><circle cx="6" cy="6" r="5" fill="none" stroke="#f0962e" stroke-width="1.3"/><ellipse cx="6" cy="6" rx="2" ry="5" fill="none" stroke="#f0962e" stroke-width="1"/><line x1="1" y1="6" x2="11" y2="6" stroke="#f0962e" stroke-width="1"/></svg>
          www.steadywave.example
        </li>
      </ul>
    </div>

    <div class="person">
      <span class="person-tab"></span>
      <div class="person-name">Marek Olenchuk,<br>P. Eng.</div>
      <div class="person-title">General Manager</div>
    </div>

    <div class="edge-band">
      <span class="band-orange"></span><span class="band-sky"></span><span class="band-purple"></span><span class="band-teal"></span>
    </div>
  </section>

  <section class="card card-back" aria-label="Card back">
    <div class="back-wordmark">STEADYWAVE<span class="back-square"></span></div>
  </section>
</main>
</body>
</html>
```